Business card design and logo for hot water plumbing business

I need a logo and business card for my business which installs hot water heaters
Must have on front:
Brightwell Hot Water Services
Gareth Pemberly
0438617204

Either front or back:
gareth@brightwellhotwaterservices.com.au
ABN 48276053816
Licence No 583420K

On the back in point form:
Supply and installation of
• electric storage
• gas storage/instantaneous
• heat pumps
• solar heaters

Iv provided 3 examples of cards I like but open to different ideas.

```html
<!DOCTYPE html>
<html lang="en">
<head>
<meta charset="utf-8">
<title>Brightwell Hot Water Services – Business Card</title>
<link rel="stylesheet" href="https://fonts.googleapis.com/css2?family=Roboto+Condensed:wght@700&family=Questrial&family=Open+Sans:wght@600&display=swap">
<style>
  :root {
    --page-bg: #ecebe8;
    --card-shadow: rgba(0, 0, 0, 0.28);
    --front-centre: #ffffff;
    --front-mid: #a9d2ef;
    --front-edge: #2b8ad3;
    --back-bg: #ffffff;
    --ink: #1e1e1e;
    --brand-ink: #3d3d3d;
    --mark-blue: #2f7fc8;
    --accent-light: #cfe8f6;
  }
  * { box-sizing: border-box; margin: 0; padding: 0; }
  html, body {
    width: 1200px;
    height: 899px;
    overflow: hidden;
  }
  body {
    background: var(--page-bg);
    position: relative;
    font-family: "Questrial", "Century Gothic", sans-serif;
    color: var(--ink);
  }
  .card {
    position: absolute;
    box-shadow: 0 6px 18px var(--card-shadow);
    overflow: hidden;
  }
  /* Front */
  .card--front {
    left: 153px;
    top: 60px;
    width: 667px;
    height: 383px;
    background: radial-gradient(ellipse 62% 68% at 46% 50%,
      var(--front-centre) 0%, var(--front-mid) 58%, var(--front-edge) 100%);
  }
  .brand {
    position: absolute;
    left: 0;
    width: 100%;
    top: 108px;
    display: flex;
    flex-direction: column;
    align-items: center;
    gap: 22px;
  }
  .brand__dot {
    width: 70px;
    height: 70px;
    border-radius: 50%;
    background: var(--mark-blue);
  }
  .brand__name {
    font-family: "Roboto Condensed", "Arial Narrow", sans-serif;
    font-weight: 700;
    font-size: 24px;
    color: var(--brand-ink);
    letter-spacing: 0.2px;
  }
  .contact-name {
    position: absolute;
    right: 62px;
    top: 280px;
    text-align: right;
    font-size: 27px;
    line-height: 38px;
  }
  /* Back */
  .card--back {
    left: 374px;
    top: 456px;
    width: 669px;
    height: 381px;
    background: var(--back-bg);
  }
  .back-accent {
    position: absolute;
    left: 50px;
    top: 80px;
    width: 270px;
    height: 270px;
    border-radius: 50%;
    background: var(--accent-light);
  }
  .details {
    position: absolute;
    left: 245px;
    top: 66px;
    font-size: 18.5px;
    line-height: 23px;
  }
  .services {
    position: absolute;
    right: 53px;
    top: 229px;
    text-align: right;
    font-family: "Open Sans", Arial, sans-serif;
    font-weight: 600;
    font-size: 19px;
    line-height: 26.5px;
  }
  .services__title { font-size: 20.5px; }
  .services__list { list-style: none; }
  .services__list li::before { content: "\2022\00a0"; }
</style>
</head>
<body>
  <section class="card card--front">
    <div class="brand">
      <span class="brand__dot"></span>
      <span class="brand__name">Brightwell Hot Water Services</span>
    </div>
    <div class="contact-name">
      <p>Gareth Pemberly</p>
      <p>0438617204</p>
    </div>
  </section>

  <section class="card card--back">
    <div class="back-accent" aria-hidden="true"></div>
    <div class="details">
      <p>gareth@brightwellhotwaterservices.com.au</p>
      <p>ABN 48276053816</p>
      <p>Licence No 583420K</p>
    </div>
    <div class="services">
      <p class="services__title">Supply and installation of</p>
      <ul class="services__list">
        <li>electric storage</li>
        <li>gas storage/instantaneous</li>
        <li>heat pumps</li>
        <li>solar heaters</li>
      </ul>
    </div>
  </section>
</body>
</html>
```